Marketing flyer to advertise course vacancies

I am seeking something that is eye catching
A document that I can edit to list our courses and prices to try and gain further bookings on the courses.
I have attached our company logo, our website is www.brightpathskills.com.au for your viewing.
Our motto is Train today for a safer tomorrow, we would want this on the brochure.

```html
<!DOCTYPE html>
<html lang="en">
<head>
<meta charset="utf-8">
<title>Upcoming August Training Courses</title>
<link href="https://fonts.googleapis.com/css2?family=Stardos+Stencil:wght@700&family=Poppins:wght@400;500;600;700&display=swap" rel="stylesheet">
<style>
  :root{
    --black:#0d0d0d;
    --red:#d9262b;
    --green:#0b7a45;
    --green-head:#0f8a4c;
    --row-light:#eeeeee;
    --row-dark:#c9c9c9;
    --ink:#222222;
    --white:#ffffff;
    --hazard:#d8b326;
    --photo-a:#a88a5c;
    --photo-b:#6d8fb8;
  }
  *{box-sizing:border-box;margin:0;padding:0}
  html,body{width:981px;height:1200px;overflow:hidden;background:var(--white)}
  body{font-family:"Poppins",sans-serif;color:var(--ink);position:relative}
  .flyer{position:relative;width:981px;height:1200px;background:var(--white)}

  .brand{position:absolute;left:0;top:0;width:470px;height:172px;display:flex;align-items:center;justify-content:center;gap:10px}
  .brand-dot{width:26px;height:26px;border-radius:50%;background:var(--green)}
  .brand-name{font-family:"Poppins",sans-serif;font-weight:700;font-size:26px;color:var(--green)}

  .hero-band{position:absolute;left:0;top:172px;width:520px;height:169px;background:var(--black);clip-path:polygon(0 0,475px 0,520px 100%,0 100%)}
  .hazard-top{position:absolute;left:0;top:172px;width:260px;height:8px;background:var(--hazard)}
  .hazard-bottom{position:absolute;left:145px;top:333px;width:375px;height:8px;background:var(--hazard)}
  .hero-title{position:absolute;left:64px;top:200px;font-family:"Stardos Stencil",serif;font-weight:700;font-size:35px;line-height:36px;color:var(--red);letter-spacing:.5px}
  .hero-rule{position:absolute;left:64px;top:287px;width:402px;height:1px;background:#777}
  .tagline{position:absolute;left:64px;top:290px;font-size:22px;color:var(--white);font-weight:400}

  .photo{position:absolute}
  .photo-team{left:430px;top:0;width:551px;height:218px;background:linear-gradient(180deg,var(--photo-b) 0%,#b89a6a 45%,var(--photo-a) 100%);clip-path:polygon(0 0,100% 0,100% 100%,48px 100%)}
  .photo-rig{left:482px;top:223px;width:236px;height:118px;background:linear-gradient(135deg,#8f9aa3,#d47a34 60%,#5b5f66);clip-path:polygon(0 0,100% 0,100% 100%,30px 100%)}
  .photo-firstaid{left:713px;top:223px;width:268px;height:118px;background:linear-gradient(135deg,#b9aa8e,#e07a2e 55%,#2d3a63);clip-path:polygon(0 0,100% 0,100% 100%,28px 100%)}

  .section-title{position:absolute;left:0;width:981px;top:358px;text-align:center;font-family:"Stardos Stencil",serif;font-weight:700;font-size:29px;color:var(--red);letter-spacing:.3px}

  .schedule{position:absolute;left:85px;top:404px;display:grid;grid-template-columns:172px 257px 171px 171px;column-gap:7px;grid-auto-rows:26px}
  .schedule .head{height:37px;background:var(--green-head);color:var(--white);font-weight:600;font-size:20px;display:flex;align-items:center;justify-content:center;border-radius:8px 8px 0 0;border-bottom:2px solid #0a5f36}
  .schedule .cell{font-size:8.3px;font-weight:600;display:flex;align-items:center;line-height:10px;border-left:1px solid #b5b5b5;border-right:1px solid #b5b5b5}
  .code{padding-left:45px}
  .name{padding-left:7px}
  .when{padding-left:9px}
  .when .d{width:54px;flex:none}
  .cost{padding-left:36px}
  .light{background:var(--row-light)}
  .dark{background:var(--row-dark)}
  .last{border-bottom:1px solid #b5b5b5}

  .footer{position:absolute;left:0;top:1103px;width:981px;height:97px;background:var(--green)}
  .footer-black{position:absolute;left:0;top:0;width:380px;height:97px;background:var(--black);clip-path:polygon(0 0,330px 0,380px 100%,0 100%)}
  .footer-edge{position:absolute;left:0;top:0;width:385px;height:97px;background:var(--white);clip-path:polygon(330px 0,336px 0,385px 100%,379px 100%)}
  .reserve{position:absolute;left:62px;top:20px;background:var(--red);color:var(--white);font-weight:600;font-size:14px;padding:2px 8px;border-radius:4px}
  .contact{position:absolute;display:flex;align-items:center;gap:5px;color:var(--white);font-size:13px}
  .contact svg{width:13px;height:13px;flex:none}
  .label{position:absolute;color:var(--white);font-weight:600;font-size:14px}
  .badge{position:absolute;left:857px;top:16px;width:170px;height:48px;border:2px solid var(--white);border-radius:6px;left:857px;width:170px}
</style>
</head>
<body>
<div class="flyer">
  <div class="brand"><span class="brand-dot"></span><span class="brand-name">BrightPath Skills</span></div>

  <div class="hero-band"></div>
  <div class="hazard-top"></div>
  <div class="hazard-bottom"></div>
  <h1 class="hero-title">SAFETY AND<br>EMERGENCY TRAINING</h1>
  <div class="hero-rule"></div>
  <p class="tagline">Train today for a safer tomorrow</p>

  <div class="photo photo-team" role="img" aria-label="Trainees in firefighting gear at an outdoor training yard"></div>
  <div class="photo photo-rig" role="img" aria-label="Workers in hard hats practising a confined space rescue"></div>
  <div class="photo photo-firstaid" role="img" aria-label="Class in hi-vis workwear practising first aid"></div>

  <h2 class="section-title">UPCOMING AUGUST TRAINING COURSES</h2>

  <div class="schedule">
    <div class="head">CODE</div><div class="head">TRAINING NAME</div><div class="head">DATE &amp; TIME</div><div class="head">COST</div>

    <div class="cell code light">CPCWHS1001</div><div class="cell name light">Prepare to Work Safely in the Construction Industry</div><div class="cell when light"><span class="d">AUG 1</span>(8.00AM-4.00PM)</div><div class="cell cost light">$80 PER PERSON</div>
    <div class="cell code dark">RIIWHS204E</div><div class="cell name dark">Work Safely at Heights</div><div class="cell when dark"><span class="d">AUG 4</span>(8.00AM- 4.30PM)</div><div class="cell cost dark">$225 PER PERSON</div>
    <div class="cell code light">RIIWHS202E</div><div class="cell name light">Enter and Work in Confined Spaces</div><div class="cell when light"><span class="d">AUG 5</span>(8.00AM- 4.00PM)</div><div class="cell cost light">$225 PER PERSON</div>
    <div class="cell code dark">PUAFER005</div><div class="cell name dark">Operate as Part of an Emergency Control Organisation (Fire Warden)</div><div class="cell when dark"><span class="d">AUG 5</span>(8.00AM- 12:30PM)</div><div class="cell cost dark">$150 PER PERSON</div>
    <div class="cell code light">CPPFES2005</div><div class="cell name light">Demonstrate First Attack Firefighting Equipment</div><div class="cell when light"><span class="d">AUG 5</span>(8.00AM- 4:30 PM)</div><div class="cell cost light">$75 PER PERSON</div>
    <div class="cell code dark">TLILIC0003</div><div class="cell name dark">Licence to Operate a Forklift Truck – Formal Training &amp; Assessment (3 days)</div><div class="cell when dark"><span class="d">AUG 6,7,8</span>(8.00AM- 4:00 PM)</div><div class="cell cost dark">$525 PER PERSON</div>
    <div class="cell code light">HLTAID011</div><div class="cell name light">Provide First Aid inc HLTAID009 Provide CPR</div><div class="cell when light"><span class="d">AUG 8</span>(8.00AM- 4:30PM)</div><div class="cell cost light">$125 PER PERSON</div>
    <div class="cell code dark">UETDREL006</div><div class="cell name dark">Working Safely Near Live Electrical Apparatus as a Non-Electrical Worker</div><div class="cell when dark"><span class="d">AUG 11</span>(8.00AM- 4:30PM)</div><div class="cell cost dark">$225 PER PERSON</div>
    <div class="cell code light">UETDRMP007</div><div class="cell name light">Perform Rescue from a Live LV Panel inc HLTAID009 Provide cardiopulmonary resuscitation (LVR CPR)</div><div class="cell when light"><span class="d">AUG 12</span>(8:00 AM - 2:00 PM)</div><div class="cell cost light">$100 PER PERSON</div>
    <div class="cell code dark">TLILIC0005</div><div class="cell name dark">Licence to Operate a EWP – Formal Training &amp; Assessment (3 days)</div><div class="cell when dark"><span class="d">AUG 13,14,15</span>(8:00 AM - 4.30PM)</div><div class="cell cost dark">$525 PER PERSON</div>
    <div class="cell code light">RIIWHS202E</div><div class="cell name light">Enter and Work in Confined Spaces and MSMWHS217 – Gas test atmospheres</div><div class="cell when light"><span class="d">AUG 15</span>(8:00 AM - 4.00PM)</div><div class="cell cost light">$300 PER PERSON</div>
    <div class="cell code dark">RIIWHS204E</div><div class="cell name dark">Work Safely at Heights</div><div class="cell when dark"><span class="d">AUG 18</span>(8:00 AM - 4.30PM)</div><div class="cell cost dark">$225 PER PERSON</div>
    <div class="cell code light">RIIWHS202E</div><div class="cell name light">Enter and Work in Confined Spaces</div><div class="cell when light"><span class="d">AUG 19</span>(8:00 AM - 4.00PM)</div><div class="cell cost light">$225 PER PERSON</div>
    <div class="cell code dark">HLTAID011</div><div class="cell name dark">Provide First Aid inc HLTAID009 Provide CPR</div><div class="cell when dark"><span class="d">AUG 20</span>(8:00 AM - 4:30PM)</div><div class="cell cost dark">$125 PER PERSON</div>
    <div class="cell code light">CPCWHS1001</div><div class="cell name light">Prepare to Work Safely in the Construction Industry (White Card) (Face to Face Training in QLD)</div><div class="cell when light"><span class="d">AUG 21</span>(8:00 AM - 4.00PM)</div><div class="cell cost light">$80 PER PERSON</div>
    <div class="cell code dark">CPCCLDG3001</div><div class="cell name dark">Licence to perform dogging training and assessment (5 days)</div><div class="cell when dark"><span class="d">AUG 18,19,<br>20,21,22</span>(8:00 AM - 4.30PM)</div><div class="cell cost dark">$1450 PER PERSON</div>
    <div class="cell code light">HLTPAT005</div><div class="cell name light">Collect Specimens for Drugs of Abuse Testing</div><div class="cell when light"><span class="d">AUG 22</span>(8:00 AM - 12:00 PM)</div><div class="cell cost light">$450 PER PERSON</div>
    <div class="cell code dark">MSMWHS216</div><div class="cell name dark">Operate Breathing Apparatus (Industrial)</div><div class="cell when dark"><span class="d">AUG 22</span>(8:00 AM - 4:30 PM)</div><div class="cell cost dark">$200 PER PERSON</div>
    <div class="cell code light">UETDREL006</div><div class="cell name light">Working Safely Near Live Electrical Apparatus as a Non-Electrical Worker</div><div class="cell when light"><span class="d">AUG 25</span>(8:00 AM - 4:30 PM)</div><div class="cell cost light">$225 PER PERSON</div>
    <div class="cell code dark">RIIMPO320F</div><div class="cell name dark">Conduct Civil Constructions Excavator Operations</div><div class="cell when dark"><span class="d">AUG 25,26</span>(8:00 AM - 4:30 PM)</div><div class="cell cost dark">$600 PER PERSON</div>
    <div class="cell code light">UETDRMP007</div><div class="cell name light">Perform Rescue from a Live LV Panel inc HLTAID009 Provide cardiopulmonary resuscitation (LVR CPR)</div><div class="cell when light"><span class="d">AUG 26</span>(8:00 AM - 2:00 PM)</div><div class="cell cost light">$100 PER PERSON</div>
    <div class="cell code dark">TLILIC0003</div><div class="cell name dark">Licence to Operate a Forklift Truck – Formal Training &amp; Assessment (3 days)</div><div class="cell when dark"><span class="d">AUG 27,28,29</span>(8:00 AM - 4.30PM)</div><div class="cell cost dark">$525 PER PERSON</div>
    <div class="cell code light">PUAFER005</div><div class="cell name light">Operate as Part of an Emergency Control Organisation (Fire Warden)</div><div class="cell when light"><span class="d">AUG 29</span>(8:00 AM - 12:30 PM)</div><div class="cell cost light">$150 PER PERSON</div>
    <div class="cell code dark last">CPPFES2005</div><div class="cell name dark last">Demonstrate First Attack Firefighting Equipment</div><div class="cell when dark last"><span class="d">AUG 29</span>(8:00 AM - 4:30 PM)</div><div class="cell cost dark last">$75 PER PERSON</div>
  </div>

  <footer class="footer">
    <div class="footer-black"></div>
    <div class="footer-edge"></div>
    <div class="reserve">RESERVE YOUR SEAT NOW</div>
    <div class="contact" style="left:62px;top:50px">
      <svg viewBox="0 0 16 16"><circle cx="8" cy="8" r="8" fill="#fff"/><rect x="3.5" y="5" width="9" height="6" fill="none" stroke="#0d0d0d" stroke-width="1.2"/><path d="M3.5 5 8 8.5 12.5 5" fill="none" stroke="#0d0d0d" stroke-width="1.2"/></svg>
      admin@brightpathskills.com.au
    </div>
    <div class="label" style="left:497px;top:20px">CALL US</div>
    <div class="contact" style="left:497px;top:39px">
      <svg viewBox="0 0 16 16"><circle cx="8" cy="8" r="8" fill="#fff"/><path d="M5 4c.8-.4 1.2 0 1.7 1.2.3.7 0 1-.5 1.4.5 1.2 1.3 2 2.4 2.5.4-.5.8-.8 1.4-.5 1.2.5 1.6 1 1.2 1.7-.6 1-1.7 1.3-3 .7C6.4 10 5 8.4 4.4 6.6 4 5.3 4.2 4.5 5 4z" fill="#0b7a45"/></svg>
      07 5550 1234
    </div>
    <div class="label" style="left:649px;top:20px">FULL SCHEDULE AT</div>
    <div class="contact" style="left:647px;top:39px">
      <svg viewBox="0 0 16 16"><circle cx="8" cy="8" r="7" fill="none" stroke="#fff" stroke-width="1.3"/><ellipse cx="8" cy="8" rx="3" ry="7" fill="none" stroke="#fff" stroke-width="1.1"/><path d="M1 8h14M2.5 4.5h11M2.5 11.5h11" stroke="#fff" stroke-width="1"/></svg>
      www.brightpathskills.com.au
    </div>
    <div class="badge" style="left:857px;width:170px;left:857px"></div>
  </footer>
</div>
</body>
</html>
```